Kids Birthday Parties Invitations

We need Kids Brevolan Birthday Party invitations.
Brevolan is a Chinese martial art (kung fu style) used exclusively for the self defense purposes so it is not a combat sport. Pallidor Brevoln organization founded in Germany further developed the art and adopted to the needs and teaching methods of the western world. Kids Brevolan is designed for kids 4 - 12 y.o. and is teaching kids how to deal with conflicts and potentially violent situations without restoring to violence and using their self-defense skills only as a last resort. We teach them to use their voice, gestures to demonstrate to others that they are not aggressive but not an easy victim
Kids Brevolan program is easy to learn and lots of FUN.
Kids Brevolan Birthday parties will be organized for the guests of the Kids Brevolan program attendees. Majority of the guests will be new to Kids Brevolan and is important that they get attracted and exited about attending the party and they understand that its about martial arts.
Kids Brevolan it's a brand and has branding restrictions on which colors can be used (branding catalog is attached).
Our prices are higher than the rest of the Martial Arts schools in a country and we are attracting wealthy families.
Text of the Invitations should be the same as on the attached invitation. Exept the contact details which are:

Limassol: 17 Mavrokordi Pelani Str, Fenwick Court (2nd floor), 3142
Nicosia: 12 Kastrinou str, Latcha, 2418
Tel: 700 412 59 Email: info@quovendra-example.com.cy
Web: www.quovendra-example.com.cy/party

The final design should communicate Fun, good mood, celebration!

The winning designer would be given further work to develop 3 fold leaflet to advertise Birthday parties, Roll standing up banner, A4 brochure and "Thank you" cards.

Kids Brevolan corporate colors are yellow, gray, black, red.

For more info re: KidsBrevolan program please see http://www.quovendra-example.com.cy/brevolan/for-kids/

Target Market(s)

Male/Female age 28-44, GreekCypriots and Russians. Parents. Employed income starting from 20 000 Euro per year and up

Industry/Entity Type

Martial Art

Font styles to use
Serif

Colors
fbed22

Requirements
Must have
• At the Kids Brevolan party birthday child will be cutting cake with the martial art sword and brake the board (one of these can be featured on the invitation).
Nice to have
• Kids Brevolan program has mascots Domu and Taroke (attached) they can be used (but not necessary).
• We bought the Birthday Party concept from QLM47 and they offer invitations (attached) however we cannot use them as they do not fit branding colors and mascots are wearing Japanese martial arts uniforms but we like their design very much (attached) if their invitation can be converted into our branding and our mascots in PBRO Kids Brevolan uniform - that would be great.

```html
<!DOCTYPE html>
<html lang="en">
<head>
<meta charset="utf-8">
<title>Kids Brevolan Birthday Party Invitation</title>
<link rel="stylesheet" href="https://fonts.googleapis.com/css2?family=Bebas+Neue&family=Nunito:wght@500;600;700&family=Oleo+Script:wght@700&family=Playfair+Display:wght@400;700&display=swap">
<style>
  :root {
    --brand-yellow: #fbed22;
    --magenta: #ff00ff;
    --ink: #111111;
    --white: #ffffff;
    --ribbon-blue: #0b3aa8;
    --ribbon-light: #7fb6dc;
  }
  * { margin: 0; padding: 0; box-sizing: border-box; }
  html, body { width: 1036px; height: 1200px; overflow: hidden; background: var(--white); }
  .invitation { position: relative; width: 1036px; height: 1200px; font-family: "Nunito", sans-serif; color: var(--ink); }

  /* ---------- Front cover ---------- */
  .cover { position: absolute; left: 0; top: 0; width: 505px; height: 1200px; overflow: hidden; }
  .cover-art { position: absolute; left: 0; top: 0; }
  .celebration-art {
    position: absolute; left: 70px; top: 265px; width: 370px; height: 620px; border-radius: 36px;
    background: linear-gradient(180deg, #f08a3a 0%, #c9652a 16%, #e8c4a2 30%, #eef2f6 46%, #4a4c52 60%, #f4f1ec 72%, #d9413a 88%, #cfcfcf 100%);
  }
  .brand-badge {
    position: absolute; left: 345px; top: 35px; width: 138px; height: 68px;
    background: var(--white); border-radius: 10px;
    display: flex; align-items: center; justify-content: center; gap: 6px;
    font-weight: 700; font-size: 17px; color: var(--ink);
  }
  .brand-badge .dot { width: 10px; height: 10px; border-radius: 50%; background: var(--brand-yellow); }
  .cover-title {
    position: absolute; left: 26px; top: 112px;
    font-family: "Playfair Display", serif; font-weight: 400; font-size: 56px; line-height: 58px;
    color: var(--ink); transform: rotate(-4deg); transform-origin: left top; letter-spacing: 1px;
  }
  .ribbon-text {
    position: absolute; left: 78px; top: 838px; width: 360px; text-align: center;
    font-family: "Playfair Display", serif; font-size: 40px; color: var(--white);
    transform: rotate(-8deg); transform-origin: center;
  }
  .party-script {
    position: absolute; left: 0; width: 505px; text-align: center;
    font-family: "Oleo Script", cursive; font-weight: 700; color: var(--ink);
    text-shadow: 2px 2px 0 var(--white), -2px -2px 0 var(--white), 2px -2px 0 var(--white), -2px 2px 0 var(--white);
  }
  .party-script.birthday { top: 920px; font-size: 104px; line-height: 120px; }
  .party-script.party { top: 1030px; font-size: 96px; line-height: 110px; padding-left: 40px; }

  /* ---------- Reply side ---------- */
  .details { position: absolute; left: 532px; top: 0; width: 504px; height: 1200px; background: var(--white); }
  .band { position: absolute; left: 0; width: 504px; background: var(--brand-yellow); }
  .band.header { top: 0; height: 281px; }
  .band.on { top: 403px; height: 40px; }
  .band.rule { top: 528px; height: 3px; }
  .band.address { top: 627px; height: 73px; }
  .band.contact { top: 1108px; height: 92px; }

  .headline { position: absolute; left: 0; width: 504px; text-align: center; font-family: "Bebas Neue", sans-serif; color: var(--ink); }
  .headline.youre { top: 48px; font-size: 86px; line-height: 80px; padding-left: 120px; }
  .headline.invited { top: 112px; font-size: 128px; line-height: 110px; letter-spacing: 4px; }
  .headline.party-for { top: 222px; font-size: 46px; line-height: 46px; letter-spacing: 7px; }

  .label { position: absolute; font-weight: 600; font-size: 21px; line-height: 24px; }
  .label.name { left: 20px; top: 308px; }
  .label.on { left: 0; width: 504px; top: 411px; text-align: center; }
  .label.date { left: 20px; top: 500px; }
  .label.time { left: 281px; top: 500px; }
  .label.rsvp { left: 256px; top: 594px; font-size: 23px; word-spacing: 4px; }

  .address-text { position: absolute; left: 0; top: 636px; width: 504px; text-align: center; font-size: 15px; line-height: 24px; font-weight: 500; }

  .release-heading { position: absolute; left: 20px; top: 728px; font-family: "Playfair Display", serif; font-weight: 700; font-size: 25px; }
  .release-note { position: absolute; left: 21px; top: 769px; font-size: 15.5px; font-weight: 500; }
  .field { position: absolute; left: 21px; width: 443px; display: flex; align-items: flex-end; font-size: 21px; font-weight: 600; height: 28px; }
  .field .line { flex: 1; border-bottom: 1.5px solid var(--ink); margin-left: 8px; margin-bottom: 4px; }
  .field.child { top: 810px; }
  .field.parent { top: 870px; }
  .field.phone { top: 930px; }
  .field.age { top: 990px; }
  .field.signature { top: 1049px; }

  .contact-text { position: absolute; left: 0; top: 1113px; width: 504px; text-align: center; font-size: 14px; line-height: 18.5px; font-weight: 600; }
  .corner { position: absolute; top: 1146px; width: 20px; height: 17px; border-bottom: 1.5px solid var(--ink); }
  .corner.left { left: 90px; border-left: 1.5px solid var(--ink); }
  .corner.right { left: 394px; border-right: 1.5px solid var(--ink); }
</style>
</head>
<body>
<main class="invitation">

  <section class="cover">
    <svg class="cover-art" width="505" height="1200" viewBox="0 0 505 1200" aria-hidden="true">
      <defs>
        <linearGradient id="cover-sky" x1="0" y1="0" x2="0" y2="1">
          <stop offset="0" stop-color="#ff00ff"/>
          <stop offset="0.45" stop-color="#ff10ee"/>
          <stop offset="0.62" stop-color="#ff4fb4"/>
          <stop offset="0.8" stop-color="#ff9a78"/>
        </linearGradient>
      </defs>
      <rect width="505" height="1200" fill="url(#cover-sky)"/>
      <polygon points="0,839 505,888 505,1200 0,1200" fill="var(--brand-yellow)"/>
    </svg>

    <div class="celebration-art" role="img" aria-label="Illustration of a cheerful boy in a party hat and club hoodie, presenting a birthday cake with candles being cut by a martial arts sword"></div>

    <svg class="cover-art" width="505" height="1200" viewBox="0 0 505 1200" aria-hidden="true">
      <polygon points="0,106 263,95 342,152 278,221 0,273" fill="var(--white)"/>
      <polygon points="33,841 120,825 124,873 48,880 58,862" fill="var(--ribbon-blue)"/>
      <polygon points="120,825 124,873 75,870" fill="var(--ribbon-light)"/>
      <polygon points="382,853 472,845 453,872 472,889 385,905" fill="var(--ribbon-blue)"/>
      <polygon points="382,853 385,905 430,873" fill="var(--ribbon-light)"/>
      <polygon points="70,863 435,810 435,866 70,919" fill="var(--ink)"/>
    </svg>

    <div class="brand-badge"><span class="dot"></span>Kids Brevolan</div>
    <h1 class="cover-title">YOU’RE<br>INVITED</h1>
    <div class="ribbon-text">To An Awesome</div>

    <div class="party-script birthday">Birthday</div>
    <div class="party-script party">party</div>
  </section>

  <section class="details">
    <div class="band header"></div>
    <div class="band on"></div>
    <div class="band rule"></div>
    <div class="band address"></div>
    <div class="band contact"></div>

    <h2 class="headline youre">YOU’RE</h2>
    <h2 class="headline invited">INVITED</h2>
    <p class="headline party-for">TO A PARTY FOR:</p>

    <p class="label name">Name:</p>
    <p class="label on">ON</p>
    <p class="label date">Date:</p>
    <p class="label time">Time:</p>
    <p class="label rsvp">RSVP by &nbsp; / &nbsp; &nbsp; /</p>

    <p class="address-text">Limassol: 17 Mavrokordi Pelani Str, Fenwick Court (2nd floor), 3142<br>Nicosia: 12 Kastrinou str, Latcha, 2418</p>

    <h3 class="release-heading">PLEASE FILL OUT RELEASE BELOW:</h3>
    <p class="release-note">This form gives permission for my child to attend a birthday party.</p>
    <div class="field child">Child’s Name:<span class="line"></span></div>
    <div class="field parent">Parent Name:<span class="line"></span></div>
    <div class="field phone">Phone:<span class="line"></span></div>
    <div class="field age">Age:<span class="line"></span></div>
    <div class="field signature">Signature:<span class="line"></span></div>

    <p class="contact-text">Tel: 700 412 59<br>Email: info@quovendra-example.com.cy<br>Web: www.quovendra-example.com.cy/party</p>
    <span class="corner left"></span>
    <span class="corner right"></span>
  </section>

</main>
</body>
</html>
```